Business Cards for wirefen.com.au
Logo already designed by Quillnoxa
Professional
Liam Forbury
Technical Engineer
Mobile: 0437 125 806
liam@wirefen.com.au
www.wirefen.com.au
Should have the text: "Cloud Application Development"

```html
<!DOCTYPE html>
<html lang="en">
<head>
<meta charset="utf-8">
<title>wirefen.com.au business card</title>
<link href="https://fonts.googleapis.com/css2?family=Arimo:ital,wght@0,400;0,700;1,700&display=swap" rel="stylesheet">
<style>
  :root {
    --page-bg: #e4e4e6;
    --card-bg: #ffffff;
    --brand-blue: #1f78c8;
    --brand-blue-dark: #0d4f95;
    --brand-blue-light: #6bb6ea;
    --ink: #3a3a3c;
    --ink-soft: #555558;
  }
  * { margin: 0; padding: 0; box-sizing: border-box; }
  html, body {
    width: 1200px; height: 988px; overflow: hidden;
    background: var(--page-bg);
    font-family: "Arimo", Arial, sans-serif;
  }
  .canvas { position: relative; width: 1200px; height: 988px; }

  .card {
    position: absolute;
    width: 590px; height: 360px;
    background: var(--card-bg);
    border-radius: 22px;
    overflow: hidden;
  }
  .card-front { left: 150px; top: 130px; }
  .card-back { left: 460px; top: 498px; }

  /* front */
  .header-band {
    position: absolute; left: 0; top: 0; width: 100%; height: 96px;
    background: linear-gradient(100deg, #d9ecf9 0%, var(--brand-blue-light) 28%, var(--brand-blue) 55%, var(--brand-blue-dark) 100%);
  }
  .identity {
    position: absolute; right: 32px; top: 18px; text-align: right; color: #fff;
  }
  .identity-name {
    font-size: 25px; font-weight: 700; font-style: italic; letter-spacing: 0.5px;
  }
  .identity-title {
    margin-top: 4px; font-size: 15px; font-weight: 700; font-style: italic;
  }
  .wordmark {
    position: absolute; left: 36px; top: 136px;
    font-size: 74px; font-weight: 700; color: var(--ink); letter-spacing: -1px;
  }
  .contacts {
    position: absolute; left: 40px; top: 258px; list-style: none;
    font-size: 15px; color: var(--ink-soft);
  }
  .contacts li { display: flex; align-items: center; height: 24px; }
  .contacts svg { width: 14px; height: 14px; margin-right: 12px; fill: var(--brand-blue); }
  .service {
    position: absolute; left: 330px; top: 258px;
  }
  .service-mark { display: block; width: 10px; height: 13px; }
  .service-text {
    margin: 7px 0 7px 0; font-size: 16px; font-weight: 700; color: var(--ink);
  }
  .service-mark.end { margin-left: 230px; }

  /* back */
  .back-mark {
    position: absolute; left: 225px; top: 62px; width: 140px; height: 140px;
    border-radius: 50%;
    background: radial-gradient(circle at 35% 30%, var(--brand-blue-light), var(--brand-blue) 55%, var(--brand-blue-dark));
  }
  .back-url {
    position: absolute; left: 0; width: 100%; top: 236px; text-align: center;
    font-size: 22px; font-weight: 700; color: var(--ink);
  }
</style>
</head>
<body>
<main class="canvas">
  <section class="card card-front" aria-label="Business card front">
    <div class="header-band" role="img" aria-label="Blue gradient header band with soft curved streaks"></div>
    <div class="identity">
      <div class="identity-name">LIAM FORBURY</div>
      <div class="identity-title">Technical Engineer</div>
    </div>
    <div class="wordmark">wirefen.com.au</div>
    <ul class="contacts">
      <li><svg viewBox="0 0 14 14"><rect x="3" y="0" width="8" height="14" rx="2"/></svg>0437 125 806</li>
      <li><svg viewBox="0 0 14 14"><rect x="0" y="2" width="14" height="10" rx="1.5"/></svg>liam@wirefen.com.au</li>
      <li><svg viewBox="0 0 14 14"><circle cx="7" cy="7" r="7"/></svg>www.wirefen.com.au</li>
    </ul>
    <div class="service">
      <svg class="service-mark" viewBox="0 0 10 13"><rect x="0" y="0" width="3" height="13" fill="#1f78c8"/><rect x="6" y="0" width="3" height="13" fill="#1f78c8"/></svg>
      <p class="service-text">Cloud Application Development</p>
      <svg class="service-mark end" viewBox="0 0 10 13"><rect x="0" y="0" width="3" height="13" fill="#1f78c8"/><rect x="6" y="0" width="3" height="13" fill="#1f78c8"/></svg>
    </div>
  </section>

  <section class="card card-back" aria-label="Business card back">
    <div class="back-mark"></div>
    <div class="back-url">www.wirefen.com.au</div>
  </section>
</main>
</body>
</html>
```